Under 16 Cricket Tour To Malaysia

I need a flyer to promote an under 16 cricket to Malaysia
The tour will run from April 25th 2108 to May the 7th

Target Market(s)

Boys aged 15-16

Industry/Entity Type

Tour

Font styles to use
Serif

Colors
0255a3
ec1f27

Requirements
Must have
• Dates of the tour
• T20 and Limited Overs games against teams from 5 other countries.
• Name of the tournament is Kestrel Bay International Under 16 Cricket Tournament
• Level 3 coaches with international experience
• Contact Marcus at marcus@pellowfield.com.au for more information.

```html
<!DOCTYPE html>
<html lang="en">
<head>
<meta charset="utf-8">
<title>Kestrel Bay International Under 16 Cricket Tournament</title>
<link href="https://fonts.googleapis.com/css2?family=Orbitron:wght@600;700;900&family=Michroma&display=swap" rel="stylesheet">
<style>
  :root {
    --stage: #e9e7ee;
    --space-dark: #0c0d16;
    --space-navy: #152447;
    --cyan: #17b5ea;
    --band: #1aa6df;
    --brand-red: #ec1f27;
    --brand-blue: #0255a3;
    --ink-outline: #0d1a3a;
    --white: #ffffff;
    --art-warm: rgba(240,120,60,.55);
    --art-pink: rgba(190,60,160,.5);
    --art-cool: rgba(60,100,210,.5);
  }
  * { box-sizing: border-box; margin: 0; padding: 0; }
  html, body { width: 1041px; height: 1200px; overflow: hidden; background: var(--stage); }
  .canvas { position: relative; width: 1041px; height: 1200px; }

  .flyer {
    position: absolute; left: 93px; top: 0; width: 854px; height: 1200px; overflow: hidden;
    font-family: "Orbitron", sans-serif; color: var(--white);
    background:
      radial-gradient(ellipse 260px 200px at 180px 300px, rgba(47,111,176,.75), transparent 70%),
      radial-gradient(ellipse 320px 220px at 470px 420px, rgba(160,35,141,.7), transparent 70%),
      radial-gradient(ellipse 260px 200px at 640px 250px, rgba(90,42,134,.7), transparent 70%),
      radial-gradient(ellipse 300px 200px at 140px 650px, rgba(47,111,176,.45), transparent 70%),
      radial-gradient(ellipse 500px 300px at 300px 120px, rgba(60,40,120,.6), transparent 70%),
      linear-gradient(180deg, var(--space-navy) 0%, #1b1640 40%, var(--space-dark) 70%, var(--space-dark) 100%);
  }

  .stripes { position: absolute; inset: 0; width: 854px; height: 1200px; }

  .hero-art {
    position: absolute; left: 610px; top: 300px; width: 244px; height: 900px;
    background: linear-gradient(180deg, var(--art-warm) 0%, var(--art-pink) 45%, var(--art-cool) 100%);
  }

  .title {
    position: absolute; left: 34px; top: 128px; width: 800px;
    transform: rotate(-8deg); transform-origin: left top;
    text-transform: uppercase; font-weight: 900; line-height: 1; letter-spacing: -1px;
    text-shadow: 2px 2px 0 var(--ink-outline), -2px -2px 0 var(--ink-outline),
                 2px -2px 0 var(--ink-outline), -2px 2px 0 var(--ink-outline), 4px 4px 0 var(--ink-outline);
  }
  .title-lead { display: block; font-size: 31px; }
  .title-main { display: block; font-size: 57px; margin-top: 8px; }
  .title-tail { display: block; font-size: 34px; text-align: right; margin-top: 6px; padding-right: 40px; }

  .dates {
    position: absolute; left: 50px; top: 345px; font-weight: 900; line-height: 1;
    text-shadow: 2px 2px 0 var(--white), -2px -2px 0 var(--white), 2px -2px 0 var(--white), -2px 2px 0 var(--white);
  }
  .date-line { display: block; color: var(--brand-red); font-size: 62px; }
  .date-line sup { color: var(--white); font-size: 34px; vertical-align: 30px; text-shadow: none; }
  .date-line.second { margin-top: 20px; }
  .date-to { color: var(--white); font-size: 28px; text-shadow: none; margin-right: 6px; }
  .date-year { display: block; color: var(--white); font-size: 62px; margin-top: 22px; text-shadow: none; }

  .feature {
    position: absolute; left: 0; width: 610px; height: 76px; background: var(--band);
    padding: 12px 20px 0 52px; font-family: "Michroma", sans-serif; font-size: 18px; line-height: 1.35;
  }
  .feature.one { top: 615px; }
  .feature.two { top: 727px; }

  .sponsors { position: absolute; left: 40px; top: 850px; display: flex; gap: 40px; align-items: center; }
  .sponsor { display: flex; flex-direction: column; align-items: center; gap: 8px; font-weight: 700; font-size: 18px; text-transform: uppercase; text-align: center; line-height: 1.25; }
  .sponsor-dot { width: 56px; height: 56px; border-radius: 50%; background: var(--brand-red); }

  .contact { position: absolute; left: 48px; top: 993px; }
  .contact-label { font-weight: 700; font-size: 28px; }
  .contact-name { font-weight: 900; font-size: 60px; color: var(--brand-red); line-height: 1.1; margin-top: 4px; }
  .contact-email { font-family: "Michroma", sans-serif; font-size: 17px; margin-top: 8px; }
</style>
</head>
<body>
<main class="canvas">
  <article class="flyer">
    <svg class="stripes" viewBox="0 0 854 1200" aria-hidden="true">
      <polygon points="0,72 445,52 0,122" fill="var(--cyan)"/>
      <polygon points="410,298 854,225 854,268" fill="var(--cyan)"/>
    </svg>

    <div class="hero-art" role="img" aria-label="Colourful painted illustration of a batsman raising the bat"></div>

    <h1 class="title">
      <span class="title-lead">Kestrel Bay International</span>
      <span class="title-main">Under 16 Cricket</span>
      <span class="title-tail">Tournament</span>
    </h1>

    <p class="dates">
      <span class="date-line">APRIL 25<sup>TH</sup></span>
      <span class="date-line second"><span class="date-to">TO</span>MAY 7<sup>TH</sup></span>
      <span class="date-year">2018</span>
    </p>

    <p class="feature one">T20 and Limited Overs games against teams from 5 other countries.</p>
    <p class="feature two">Level 3 coaches with international experience</p>

    <div class="sponsors">
      <span class="sponsor"><span class="sponsor-dot"></span>Pellowfield Sports</span>
      <span class="sponsor">Harbourline Sport<br>Westmere</span>
    </div>

    <div class="contact">
      <p class="contact-label">Contact</p>
      <p class="contact-name">Marcus</p>
      <p class="contact-email">marcus@pellowfield.com.au</p>
    </div>
  </article>
</main>
</body>
</html>
```